Spring 2026 Deck Construction Direct Mail Flier

The logo files I will include were named "birchwood valley handymen" by the digital artist. However, my company is called Birchwood Valley Yardcraft (That was not a typo. There is no space between "home" and "service") If you'd like to experiment with color modification of the logo to make it fit better with designs you come up with, please be my guest.

I need a 6"x12" flier design to market my deck construction business. The expected goal is to get phone calls and book appointments for the upcoming Spring 2026 construction season. The call to action being something along the lines of "Call now; Appointments are going fast!"

My target audience is upper middle class (annual household income $100,000 - $200,000) families of 3-5 in the capital region of New York state, US. Houses are most commonly either vinyl sided, or sometimes a combination of vinyl siding and brick. The ideal flier design will feature this type of house. Also most houses in my target area have nice lawns with mulched gardens as well.

I prefer designs with more sweeping, gradual curves than sharp square edges and corners, though some squares and corners are ok. I like designs with pallets consisting of blue, red, green, black, gray. I do not like purple, pink, yellow, or orange.

If it's possible and will fit, it would be nice to have images of pressure treated lumber, western cedar decking, and composite decking, so that customers understand I can provide any of the three. Also listing them out would be great.

I prefer designs that are more visual than text-based. On at least one side the dominant element should be a visual of a large composite or cedar deck. An image somewhere - wherever it can fit - of a small (10'x14' or so), basic deck of pressure treated lumber would be ideal as well so that potential clients know I will build those. Also I would like some element, on either side, that creates a sense of urgency by drawing the eye to text along the lines of "2026 appointments are filling fast. Book your free consultation today!"

Selling points:
- Veteran owned and operated
- Hometown feel
- Personal service
- Satisfaction guaranteed

I will use the Northgate General Parcel Corps's "Neighbor Route Drop Delivery" (NRDD) service to deliver these, so on either the front or back there should be a small amount of reserved space in the top right corner for the NGPC's required markings (see https://www.lanternhillprint.com/products/electrician-repair-nrdd-postcard?variant=81736254190 for an example of the amount of space required). It's ok if there is imagery there and it gets covered up by the NGPC markings, it just shouldn't be anything important. You do not have to include the NGPC markings themselves. My print guy will do that when I pass him this design.

A final note on this; I've mentioned Spring 2026 several times. But I do not want the design to be relevant only for Spring. I'd like to use the design throughout the year so please no hard references to Spring that will make the flier seem out of place in the fall.

Thank you very much. I appreciate your time.

```html
<!DOCTYPE html>
<html lang="en">
<head>
<meta charset="utf-8">
<title>Birchwood Valley Yardcraft – Deck Flier</title>
<link href="https://fonts.googleapis.com/css2?family=Barlow:wght@400;500;600&family=Barlow+Semi+Condensed:wght@600;700;800&display=swap" rel="stylesheet">
<style>
:root{
  --navy:#17355f;
  --navy-dark:#12284a;
  --red:#b3212a;
  --green:#7cb342;
  --gold:#d9a82a;
  --ink:#27303b;
  --white:#ffffff;
  --stage:#e9e9e9;
}
*{box-sizing:border-box;margin:0;padding:0}
html,body{width:1200px;height:653px;overflow:hidden;background:var(--stage)}
body{position:relative;font-family:"Barlow",sans-serif}
.card{position:absolute;top:184px;width:570px;height:285px;overflow:hidden;background:var(--white);box-shadow:0 2px 6px rgba(0,0,0,.18)}
.card--front{left:18px}
.card--back{left:612px}
.layer{position:absolute;inset:0}
.photo{position:absolute}
.round-photo{position:absolute;border-radius:50%;border:3px solid var(--red);box-shadow:0 0 0 2px var(--white),0 2px 5px rgba(0,0,0,.3)}
.headline{position:absolute;font-family:"Barlow Semi Condensed",sans-serif;font-weight:800;line-height:1;white-space:nowrap}
.pill{position:absolute;height:18px;border-radius:9px;background:var(--green);color:var(--white);font-weight:500;font-size:12.5px;line-height:18px;text-align:center;white-space:nowrap}
.brand{position:absolute;display:flex;align-items:center;gap:5px;font-family:"Barlow Semi Condensed",sans-serif;font-weight:700;line-height:1.05}
.brand__dot{flex:none;border-radius:50%}
.checklist{position:absolute;list-style:none;white-space:nowrap}
.checklist li{display:flex;align-items:center;gap:5px}
.checklist svg{flex:none}
.seal{position:absolute;border-radius:50%;background:radial-gradient(circle at 40% 35%,#f3d06a,var(--gold) 60%,#a97c16);border:3px solid #f4e1a0}
.seal__core{position:absolute;inset:14px;border-radius:50%;background:var(--red)}
.footer-bar{position:absolute;left:0;right:0;bottom:0;height:31px;background:var(--navy-dark);border-top:2px solid var(--red);display:flex;align-items:center;color:var(--white);white-space:nowrap}
.footer-bar__divider{width:1px;height:19px;background:rgba(255,255,255,.7);margin:0 6px}
.footer-bar__phone{display:flex;align-items:center;gap:4px;font-family:"Barlow Semi Condensed",sans-serif;font-weight:700}
.postal{position:absolute;border:1.5px solid var(--ink);color:var(--ink);font-size:4.3px;line-height:1.05;text-align:center;background:var(--white)}
</style>
</head>
<body>

<!-- FRONT -->
<section class="card card--front">
  <div class="photo" role="img" aria-label="Large cedar deck under a timber pergola with green hedges and lawn behind" style="left:0;top:0;width:570px;height:230px;background:
    linear-gradient(180deg,rgba(40,60,30,.55) 0%,rgba(40,60,30,0) 30%),
    linear-gradient(100deg,#5b4030 0%,#7d5a42 22%,#8c7a5c 40%,#6f8a58 55%,#a88d72 72%,#c2ad98 100%)"></div>
  <div class="layer" style="background:linear-gradient(90deg,rgba(20,20,20,.35),rgba(20,20,20,0) 70%)"></div>

  <svg class="layer" viewBox="0 0 570 285" width="570" height="285" aria-hidden="true">
    <defs>
      <linearGradient id="grayBand" x1="0" x2="1" y1="0" y2="0">
        <stop offset="0" stop-color="#d3d5d8"/><stop offset="1" stop-color="#7f8388"/>
      </linearGradient>
    </defs>
    <path d="M190 150 C320 90 450 78 570 74 L570 90 C450 94 330 110 190 150Z" fill="#1c1c1c" opacity=".85"/>
    <path d="M170 170 C300 112 440 98 570 94 L570 140 C450 138 320 150 170 170Z" fill="var(--red)"/>
    <path d="M0 200 C120 160 260 140 570 142 L570 254 L0 254Z" fill="url(#grayBand)"/>
    <path d="M0 205 C100 170 200 158 300 156 C200 170 120 200 0 254Z" fill="var(--navy)"/>
    <path d="M60 254 C170 190 330 168 570 170 L570 254Z" fill="var(--white)"/>
  </svg>

  <h1 class="headline" style="left:28px;top:25px;font-size:37px;color:var(--white);letter-spacing:-.2px">YOUR HOME, OUR EXPERTISE</h1>
  <span class="pill" style="left:28px;top:64px;width:94px">Composite</span>
  <span class="pill" style="left:127px;top:64px;width:60px">Cedar</span>
  <span class="pill" style="left:192px;top:64px;width:152px">Pressure Treated Lumber</span>

  <div class="brand" style="left:478px;top:34px;width:86px;color:var(--white);font-size:12.5px">
    <span class="brand__dot" style="width:12px;height:12px;background:var(--white)"></span>
    <span>Birchwood Valley Yardcraft</span>
  </div>

  <div class="round-photo photo" role="img" aria-label="Small basic pressure treated deck with railing beside a green lawn and trees" style="left:25px;top:130px;width:110px;height:110px;background:linear-gradient(180deg,#2f5a26 0%,#4f7a34 38%,#b5683a 52%,#d98c4c 75%,#e6a060 100%)"></div>
  <div class="round-photo photo" role="img" aria-label="Cedar deck with wicker chairs and a wooden privacy fence" style="left:146px;top:130px;width:110px;height:110px;background:linear-gradient(180deg,#7f8f4a 0%,#b08a58 35%,#9d7a4c 55%,#c9a27a 75%,#dcbc98 100%)"></div>
  <div class="round-photo photo" role="img" aria-label="Deck with dining table beside a brick and vinyl sided house" style="left:266px;top:130px;width:110px;height:110px;background:linear-gradient(180deg,#9cbbd8 0%,#a4583f 30%,#e6ddd0 45%,#8a6a4c 60%,#c7a27c 100%)"></div>

  <div class="seal" style="left:428px;top:134px;width:66px;height:66px"><div class="seal__core"></div></div>

  <ul class="checklist" style="left:393px;top:206px;font-size:10.5px;color:var(--ink);font-weight:500;line-height:12px">
    <li><svg width="9" height="9" viewBox="0 0 10 10"><circle cx="5" cy="5" r="4.2" fill="none" stroke="var(--red)" stroke-width="1.1"/><path d="M2.9 5.1l1.5 1.5 3-3.3" fill="none" stroke="var(--red)" stroke-width="1.2"/></svg>Veteran Owned &amp; Operated</li>
    <li><svg width="9" height="9" viewBox="0 0 10 10"><circle cx="5" cy="5" r="4.2" fill="none" stroke="var(--red)" stroke-width="1.1"/><path d="M2.9 5.1l1.5 1.5 3-3.3" fill="none" stroke="var(--red)" stroke-width="1.2"/></svg>Personal Service</li>
    <li><svg width="9" height="9" viewBox="0 0 10 10"><circle cx="5" cy="5" r="4.2" fill="none" stroke="var(--red)" stroke-width="1.1"/><path d="M2.9 5.1l1.5 1.5 3-3.3" fill="none" stroke="var(--red)" stroke-width="1.2"/></svg>Satisfaction Guaranteed</li>
  </ul>

  <footer class="footer-bar" style="padding-left:24px;font-size:14px">
    <span>2026 appointments are filling fast. Book your free consultation today!</span>
    <span class="footer-bar__divider"></span>
    <span class="footer-bar__phone" style="font-size:15px">
      <svg width="10" height="10" viewBox="0 0 24 24"><path d="M6.6 10.8a15 15 0 0 0 6.6 6.6l2.2-2.2c.3-.3.7-.4 1-.2 1.1.4 2.3.6 3.6.6.6 0 1 .4 1 1V20c0 .6-.4 1-1 1A17 17 0 0 1 3 4c0-.6.4-1 1-1h3.5c.6 0 1 .4 1 1 0 1.3.2 2.5.6 3.6.1.3 0 .7-.2 1z" fill="var(--red)"/></svg>
      555 014 2276
    </span>
  </footer>
</section>

<!-- BACK -->
<section class="card card--back">
  <div class="photo" role="img" aria-label="Large composite deck with covered outdoor lounge, dining area and garden plantings" style="left:0;top:0;width:320px;height:175px;background:
    linear-gradient(180deg,rgba(255,255,255,0) 55%,#fff 100%),
    linear-gradient(100deg,#3f2e22 0%,#6b4a34 25%,#8a6a50 45%,#5f7a46 62%,#b59c80 80%,#cdbba6 100%)"></div>
  <div class="photo" role="img" aria-label="Wooden deck boards and railing in sunlight" style="left:320px;top:100px;width:250px;height:154px;background:linear-gradient(180deg,rgba(255,255,255,0) 0%,#cfb18a 35%,#b08f66 70%,#9c7b55 100%)"></div>
  <div class="photo" role="img" aria-label="Stack of pressure treated lumber" style="left:302px;top:28px;width:152px;height:80px;border-radius:6px;background:linear-gradient(160deg,#ecd1a6 0%,#d8b482 45%,#bd9566 80%,#8f9a5a 100%)"></div>

  <svg class="layer" viewBox="0 0 570 285" width="570" height="285" aria-hidden="true">
    <path d="M252 0 L282 0 C300 40 310 90 336 122 L318 126 C294 92 276 42 252 0Z" fill="var(--navy)"/>
    <path d="M318 126 L336 122 C338 125 340 127 342 129 L322 132Z" fill="var(--red)"/>
  </svg>

  <div class="postal" style="left:476px;top:33px;width:62px;height:28px;padding-top:3px">PRESORTED STANDARD<br>NGPC POSTAGE PAID<br>2NEIGHBORROUTE<br><span style="font-size:7px;font-weight:600">ECRWSS</span></div>
  <div class="postal" style="left:476px;top:65px;width:62px;height:17px;padding:3px 0 0 4px;text-align:left">LOCAL<br>POSTAL CUSTOMER</div>

  <h2 class="headline" style="left:24px;top:110px;font-size:23.5px;color:var(--navy);line-height:.98">UPGRADE YOUR<br><span style="color:var(--red)">OUTDOOR LIVING SPACE</span></h2>

  <span class="pill" style="left:0;top:157px;width:160px;height:19px;line-height:19px;border-radius:0 10px 10px 0;font-size:13px;text-align:left;padding-left:24px;font-weight:600">We design and build</span>

  <ul class="checklist" style="left:26px;top:183px;font-size:13.5px;color:var(--ink);line-height:20.5px">
    <li><svg width="10" height="10" viewBox="0 0 10 10"><circle cx="5" cy="5" r="4.2" fill="none" stroke="var(--red)" stroke-width="1.1"/><path d="M2.9 5.1l1.5 1.5 3-3.3" fill="none" stroke="var(--red)" stroke-width="1.2"/></svg>Composite Decks</li>
    <li><svg width="10" height="10" viewBox="0 0 10 10"><circle cx="5" cy="5" r="4.2" fill="none" stroke="var(--red)" stroke-width="1.1"/><path d="M2.9 5.1l1.5 1.5 3-3.3" fill="none" stroke="var(--red)" stroke-width="1.2"/></svg>Western Cedar Decks</li>
    <li><svg width="10" height="10" viewBox="0 0 10 10"><circle cx="5" cy="5" r="4.2" fill="none" stroke="var(--red)" stroke-width="1.1"/><path d="M2.9 5.1l1.5 1.5 3-3.3" fill="none" stroke="var(--red)" stroke-width="1.2"/></svg>Pressure Treated Decks</li>
  </ul>

  <div class="brand" style="left:200px;top:186px;width:76px;color:var(--navy);font-size:12.5px">
    <span class="brand__dot" style="width:11px;height:11px;background:var(--red)"></span>
    <span>Birchwood Valley Yardcraft</span>
  </div>

  <div class="round-photo photo" role="img" aria-label="Pressure treated deck with patio table, chairs and grill before green trees" style="left:281px;top:113px;width:126px;height:126px;background:linear-gradient(180deg,#3c6a2e 0%,#5f8a40 38%,#a87445 55%,#c98c52 80%,#d99a60 100%)"></div>
  <div class="round-photo photo" role="img" aria-label="Dark stained cedar deck with pergola shadows" style="left:419px;top:113px;width:126px;height:126px;background:linear-gradient(180deg,#9a5a3a 0%,#5a3a2a 35%,#3f2c22 65%,#6b4a36 100%)"></div>

  <footer class="footer-bar" style="padding-left:24px;font-size:14px">
    <span>Call now, Appointments are going fast!</span>
    <span class="footer-bar__divider" style="margin:0 6px 0 11px"></span>
    <span class="footer-bar__phone" style="font-size:15px">
      <svg width="10" height="10" viewBox="0 0 24 24"><path d="M6.6 10.8a15 15 0 0 0 6.6 6.6l2.2-2.2c.3-.3.7-.4 1-.2 1.1.4 2.3.6 3.6.6.6 0 1 .4 1 1V20c0 .6-.4 1-1 1A17 17 0 0 1 3 4c0-.6.4-1 1-1h3.5c.6 0 1 .4 1 1 0 1.3.2 2.5.6 3.6.1.3 0 .7-.2 1z" fill="var(--red)"/></svg>
      555 014 2276
    </span>
    <span style="margin:0 3px">|</span>
    <span style="font-size:9.5px;font-weight:500">www.birchwoodvalleyyardcraft.com</span>
  </footer>
</section>

</body>
</html>
```